Business Card Design Project 4 Construction Business

I am after a creative, but sleek and simple/ clean business card design. This design will form the basis of future items and might include a logo or simply a creative way to lay out the text of my company name 'kestrel ventures'
I like the simplicity of black and white however I would also be happy to see a splash of colour introduced somehow to give the text some interest and make it stand out.
I would like a double sided card.
I am young (ish!) and professional, offering construction and project management services, what I don't want is the traditional builders type card featuring a cheesy hammer/ saw image etc.
As the company name, kestrel ventures, suggests, we focus on working closely and collaboratively together, in synergy with all stakeholders involved in the projects that we undertake
Construction

```html
<!DOCTYPE html>
<html lang="en">
<head>
<meta charset="utf-8">
<title>Kestrel Ventures – Business Card</title>
<link rel="stylesheet" href="https://fonts.googleapis.com/css2?family=Michroma&family=Roboto+Condensed:ital,wght@0,400;0,700;1,700&display=swap">
<style>
  :root {
    --backdrop: #262a2b;
    --ink: #111111;
    --ink-soft: #333333;
    --accent: #8e0d0d;
    --rule: #777777;
  }
  html, body {
    margin: 0;
    width: 1200px;
    height: 1200px;
    overflow: hidden;
    background: var(--backdrop);
  }
  .stage { position: relative; width: 1200px; height: 1200px; }
  .card { position: absolute; top: 440px; width: 535px; height: 321px; }
  .card--front { left: 41px; }
  .card--back { left: 625px; }
  .card svg { display: block; width: 100%; height: 100%; }
  .wordmark { font-family: "Michroma", sans-serif; fill: var(--ink); }
  .info { font-family: "Roboto Condensed", sans-serif; fill: var(--ink-soft); }
  .info--name { fill: var(--accent); font-size: 21px; }
  .info--title { font-size: 16px; }
  .info--address { font-size: 14px; letter-spacing: 1.6px; }
  .info--contact { font-size: 14px; }
  .info--web { font-weight: 700; font-style: italic; }
  .info--web .accent { fill: var(--accent); }
</style>
</head>
<body>
<main class="stage">
  <svg width="0" height="0" style="position:absolute" aria-hidden="true">
    <defs>
      <linearGradient id="brushed-silver" x1="0" y1="0" x2="1" y2="0.6">
        <stop offset="0" stop-color="#b9b9b9"/>
        <stop offset="0.15" stop-color="#f4f4f4"/>
        <stop offset="0.3" stop-color="#a9a9a9"/>
        <stop offset="0.5" stop-color="#ececec"/>
        <stop offset="0.65" stop-color="#b5b5b5"/>
        <stop offset="0.8" stop-color="#f6f6f6"/>
        <stop offset="1" stop-color="#b0b0b0"/>
      </linearGradient>
      <linearGradient id="brushed-red" x1="0" y1="0" x2="1" y2="0.6">
        <stop offset="0" stop-color="#3a0000"/>
        <stop offset="0.2" stop-color="#8a0808"/>
        <stop offset="0.35" stop-color="#2a0000"/>
        <stop offset="0.55" stop-color="#930b0b"/>
        <stop offset="0.75" stop-color="#220000"/>
        <stop offset="1" stop-color="#8c0707"/>
      </linearGradient>
      <linearGradient id="plate-face" x1="0" y1="0" x2="1" y2="1">
        <stop offset="0" stop-color="#e4e4e4"/>
        <stop offset="0.4" stop-color="#ffffff"/>
        <stop offset="1" stop-color="#dcdcdc"/>
      </linearGradient>
      <linearGradient id="plate-rim" x1="0" y1="0" x2="0" y2="1">
        <stop offset="0" stop-color="#f0f0f0"/>
        <stop offset="0.5" stop-color="#9a9a9a"/>
        <stop offset="1" stop-color="#e8e8e8"/>
      </linearGradient>
      <radialGradient id="screw-head" cx="0.4" cy="0.35" r="0.7">
        <stop offset="0" stop-color="#e0e0e0"/>
        <stop offset="1" stop-color="#808080"/>
      </radialGradient>
      <g id="screw">
        <circle r="13" fill="url(#screw-head)" stroke="#777" stroke-width="1"/>
        <line x1="-11" y1="3" x2="11" y2="-3" stroke="#666" stroke-width="2"/>
      </g>
      <g id="plate">
        <rect x="46" y="44" width="520" height="279" rx="40" fill="url(#plate-rim)"/>
        <rect x="54" y="52" width="504" height="263" rx="34" fill="url(#plate-face)" stroke="#bdbdbd" stroke-width="1"/>
        <use href="#screw" x="91" y="90"/>
        <use href="#screw" x="522" y="90"/>
        <use href="#screw" x="91" y="278"/>
        <use href="#screw" x="522" y="278"/>
      </g>
    </defs>
  </svg>

  <section class="card card--front" aria-label="Card front">
    <svg viewBox="0 0 613 368">
      <rect width="613" height="368" fill="url(#brushed-silver)"/>
      <use href="#plate"/>
      <text class="wordmark" x="306" y="178" text-anchor="middle" font-size="38">KESTREL</text>
      <text class="wordmark" x="306" y="224" text-anchor="middle" font-size="22" letter-spacing="12">VENTURES</text>
    </svg>
  </section>

  <section class="card card--back" aria-label="Card back">
    <svg viewBox="0 0 613 368">
      <rect width="613" height="368" fill="url(#brushed-red)"/>
      <use href="#plate"/>
      <text class="info info--name" x="188" y="181" text-anchor="end">Alex REED</text>
      <text class="info info--title" x="188" y="204" text-anchor="end">Director</text>
      <line x1="200" y1="155" x2="200" y2="216" stroke="var(--rule)" stroke-width="1"/>
      <text class="info info--address" x="213" y="171">dummy dummy</text>
      <text class="info info--address" x="213" y="190" letter-spacing="0.2">dummy dummy City</text>
      <text class="info info--address" x="213" y="209">dummy Country</text>
      <line x1="344" y1="155" x2="344" y2="216" stroke="var(--rule)" stroke-width="1"/>
      <text class="info info--contact" x="357" y="171">(083) 5550147</text>
      <text class="info info--contact" x="357" y="190">alex@kestrelventures.com</text>
      <text class="info info--contact info--web" x="357" y="209">www.<tspan class="accent">kestrelventures</tspan>.com</text>
    </svg>
  </section>
</main>
</body>
</html>
```